Construction Company

I'm a new construction company called Tembrik Construction. I want my card to look simple and clean. I have provided a sample of what I want the front to look like (Tembrik_Card.jpeg) and a back ground for the back of the (Tembrik_Card_Background.jpeg) - the background can be faded so my name and other information is more prominent.
Construction

```html
<!DOCTYPE html>
<html lang="en">
<head>
<meta charset="utf-8">
<title>Tembrik Construction – Business Card</title>
<link rel="stylesheet" href="https://fonts.googleapis.com/css2?family=Quicksand:wght@500;600&display=swap">
<style>
  :root {
    --page-bg: #f4f4f4;
    --card-black: #0b0b0c;
    --card-edge: #1a1b1d;
    --band-dark: #101419;
    --band-light: #4a5866;
    --accent: #f29a1f;
    --text-grey: #c9c9c9;
    --shadow: rgba(0, 0, 0, 0.28);
  }
  * { box-sizing: border-box; margin: 0; padding: 0; }
  html, body {
    width: 1200px;
    height: 800px;
    overflow: hidden;
    background: var(--page-bg);
    font-family: "Quicksand", "Helvetica Neue", Arial, sans-serif;
  }
  .stage {
    position: relative;
    width: 1200px;
    height: 800px;
  }
  .card {
    position: absolute;
    top: 250px;
    width: 525px;
    height: 300px;
    background: radial-gradient(ellipse at 55% 45%, var(--card-edge) 0%, var(--card-black) 70%);
    box-shadow: 0 10px 28px var(--shadow);
    overflow: hidden;
  }
  .card--contact { left: 50px; }
  .card--brand { left: 625px; }

  /* Contact side */
  .texture-band {
    position: absolute;
    left: 0;
    right: 0;
    top: 78px;
    height: 150px;
    background:
      radial-gradient(ellipse at 62% 55%, var(--band-light) 0%, rgba(74, 88, 102, 0) 55%),
      linear-gradient(180deg, var(--band-dark) 0%, #1b222a 50%, var(--band-dark) 100%);
    border-top: 1px solid #2a3038;
    border-bottom: 1px solid #2a3038;
  }
  .wordmark {
    color: var(--accent);
    font-weight: 500;
    text-transform: uppercase;
    line-height: 1;
  }
  .card--contact .wordmark {
    position: absolute;
    left: 34px;
    top: 92px;
  }
  .card--contact .wordmark-main { font-size: 40px; letter-spacing: 9px; }
  .card--contact .wordmark-sub { font-size: 11px; letter-spacing: 7.4px; margin-top: 6px; }

  .contact {
    position: absolute;
    right: 30px;
    bottom: 40px;
    text-align: left;
  }
  .contact-name {
    color: var(--accent);
    font-size: 24px;
    font-weight: 500;
    letter-spacing: 3px;
    text-transform: uppercase;
    margin-bottom: 8px;
  }
  .contact-line {
    display: flex;
    align-items: center;
    gap: 7px;
    color: var(--text-grey);
    font-size: 13px;
    font-weight: 500;
    margin-bottom: 3px;
  }
  .contact-icon { width: 12px; height: 12px; flex: none; }

  /* Brand side */
  .card--brand .wordmark {
    position: absolute;
    left: 0;
    right: 0;
    top: 106px;
    text-align: center;
  }
  .card--brand .wordmark-main { font-size: 58px; letter-spacing: 14px; padding-left: 14px; }
  .card--brand .wordmark-sub { font-size: 14px; letter-spacing: 11px; padding-left: 11px; margin-top: 10px; }
</style>
</head>
<body>
<main class="stage">

  <section class="card card--contact" aria-label="Business card, contact side">
    <div class="texture-band" role="img" aria-label="Faded dark metal mesh background texture"></div>
    <div class="wordmark">
      <div class="wordmark-main">Tembrik</div>
      <div class="wordmark-sub">Construction</div>
    </div>
    <div class="contact">
      <p class="contact-name">Your Name</p>
      <p class="contact-line">
        <svg class="contact-icon" viewBox="0 0 12 12" aria-hidden="true">
          <rect width="12" height="12" rx="2" fill="var(--accent)"/>
          <path d="M3.4 2.6 L5 4.4 L4.2 5.3 C4.7 6.3 5.6 7.2 6.7 7.8 L7.6 7 L9.4 8.6 L8.5 9.6 C5.8 9.2 2.8 6.2 2.4 3.5 Z" fill="var(--card-black)"/>
        </svg>
        000-000-000
      </p>
      <p class="contact-line">
        <svg class="contact-icon" viewBox="0 0 12 12" aria-hidden="true">
          <rect width="12" height="12" rx="2" fill="var(--accent)"/>
          <rect x="2.2" y="3.4" width="7.6" height="5.2" fill="none" stroke="var(--card-black)" stroke-width="1"/>
          <path d="M2.2 3.4 L6 6.4 L9.8 3.4" fill="none" stroke="var(--card-black)" stroke-width="1"/>
        </svg>
        Email@
      </p>
    </div>
  </section>

  <section class="card card--brand" aria-label="Business card, brand side">
    <div class="wordmark">
      <div class="wordmark-main">Tembrik</div>
      <div class="wordmark-sub">Construction</div>
    </div>
  </section>

</main>
</body>
</html>
```